KRTLO Promotion Flyer to raise money and communicate our goals

We need a flyer that promotes our organization. We are a 501(c)3 trying to raise money for Arts, Education and Entrepreneurship in our small town.

We promote a social events that improve qualtiy of life and educate people on how to start and expand businesses. Our goal is to make downtown an active and thriving place with many things for people to do and enjoy as well as create a favorable place for business.

Target Market(s)

Wealthy donors and Organizations with cash

Industry/Entity Type

Education

Colors

Designer to choose colors to be used in the design.

Requirements
Must have
• Eye catching graphics and look very professional
• Should appeal to men and women
Nice to have
• Make use of any known psychological colors and fonts etc... that appeal to philanthropic people
Should not have
• Should not be complicated or confusing

```html
<!DOCTYPE html>
<html lang="en">
<head>
<meta charset="utf-8">
<title>KRTLO Membership Flyer</title>
<link href="https://fonts.googleapis.com/css2?family=Open+Sans:wght@400;600;700&display=swap" rel="stylesheet">
<style>
  :root {
    --backdrop: #3b3b3d;
    --paper: #ffffff;
    --green: #7cb342;
    --green-deep: #6fa536;
    --panel: #1f2630;
    --text-light: #ffffff;
    --text-soft: #e8eef2;
    --forest-dark: #2f4a22;
    --forest-mid: #5f7f3a;
    --forest-light: #d9d3a8;
    --sky-glow: #f3ecd0;
  }
  * { margin: 0; padding: 0; box-sizing: border-box; }
  html, body { width: 1200px; height: 1200px; overflow: hidden; }
  body {
    background: var(--backdrop);
    font-family: "Open Sans", Arial, sans-serif;
    position: relative;
  }
  .flyer {
    position: absolute;
    left: 175px; top: 50px;
    width: 850px; height: 1100px;
    background: var(--paper);
    overflow: hidden;
    box-shadow: 0 8px 24px rgba(0,0,0,.45);
  }
  .hero-forest {
    position: absolute; left: 0; top: 0; width: 850px; height: 521px;
    background:
      radial-gradient(ellipse 260px 220px at 62% 18%, var(--sky-glow) 0%, rgba(243,236,208,0) 100%),
      linear-gradient(180deg, var(--forest-light) 0%, #b7b48a 35%, var(--forest-mid) 65%, var(--forest-dark) 100%);
  }
  .brand-box {
    position: absolute; left: 62px; top: 0; width: 232px; height: 167px;
    background: var(--paper);
    display: flex; align-items: center; justify-content: center; gap: 12px;
  }
  .brand-mark { width: 22px; height: 22px; background: var(--green); }
  .brand-name {
    font-weight: 700; font-size: 40px; color: var(--panel); letter-spacing: 1px;
  }
  .band {
    position: absolute; left: 0; width: 850px; background: var(--green);
  }
  .band-intro { top: 521px; height: 204px; }
  .band-appeal { top: 928px; height: 172px; }
  .place-photo {
    position: absolute; top: 445px; height: 149px;
    border: 4px solid var(--paper);
    box-shadow: 0 2px 4px rgba(0,0,0,.25);
  }
  .photo-hall { left: 32px; width: 297px; background: linear-gradient(180deg, #b9cde0 0%, #cfc6b8 50%, #6f9a4a 100%); }
  .photo-sign { left: 350px; width: 136px; background: linear-gradient(180deg, #c9d4de 0%, #7a2e2a 45%, #6b3a2c 75%, #9ea39a 100%); }
  .photo-pavilion { left: 507px; width: 296px; background: linear-gradient(180deg, #8fb6dc 0%, #d8d2c4 45%, #8a3a2a 70%, #b3a995 100%); }
  .intro-text {
    position: absolute; left: 40px; top: 622px; width: 770px;
    text-align: center; color: var(--text-light);
    font-size: 15.5px; line-height: 1.32;
  }
  .mission-panel {
    position: absolute; left: 0; top: 725px; width: 850px; height: 203px;
    background: var(--panel);
  }
  .mission-item { position: absolute; width: 300px; color: var(--text-soft); font-size: 17px; line-height: 1.3; }
  .mission-item strong { color: var(--green); font-weight: 700; }
  .mission-icon { position: absolute; width: 34px; height: 34px; }
  .appeal-text {
    position: absolute; left: 30px; top: 952px; width: 790px;
    text-align: center; color: var(--text-light);
    font-size: 14.6px; line-height: 1.3;
  }
</style>
</head>
<body>
  <main class="flyer">
    <div class="hero-forest" role="img" aria-label="Sunlit pine forest with mossy green floor"></div>

    <div class="brand-box">
      <span class="brand-mark"></span>
      <span class="brand-name">KRTLO</span>
    </div>

    <div class="band band-intro"></div>

    <div class="place-photo photo-hall" role="img" aria-label="Town event hall with lawn and trees"></div>
    <div class="place-photo photo-sign" role="img" aria-label="Town welcome sign with holiday message"></div>
    <div class="place-photo photo-pavilion" role="img" aria-label="Open-sided pavilion with red roof"></div>

    <p class="intro-text">The Pine Hollow Small Business Association (KRTLO) is a local leader in the areas of Arts, Education and Entrepreneurship and is working diligently to promote Pine Hollow and revitalize our downtown. When you become an KRTLO Member, you will be a part of the citywide work that the KRTLO does every day to improve the lives of citizens of Pine Hollow:</p>

    <section class="mission-panel">
      <svg class="mission-icon" style="left:46px;top:30px" viewBox="0 0 34 34" aria-hidden="true">
        <path d="M4 13h6l14-8v24l-14-8H4z" fill="var(--green)"/>
        <path d="M9 21l3 9h4l-2-9z" fill="var(--green)"/>
        <path d="M27 12l4-3M27 17h5M27 22l4 3" stroke="var(--green)" stroke-width="2" fill="none"/>
      </svg>
      <p class="mission-item" style="left:108px;top:16px"><strong>We promote</strong> Pine Hollow Hotels, Shopping and Events that make Pine Hollow a pleasant, exciting and prosperous place to live.</p>

      <svg class="mission-icon" style="left:46px;top:122px" viewBox="0 0 34 34" aria-hidden="true">
        <ellipse cx="20" cy="8" rx="6" ry="2.5" fill="var(--green)"/>
        <ellipse cx="20" cy="13" rx="6" ry="2.5" fill="var(--green)"/>
        <path d="M2 20h6l6 2h8c2 0 2 3 0 3h-8M8 28l10 2 14-8c1-2-1-3-3-2l-8 4" stroke="var(--green)" stroke-width="2.4" fill="none" stroke-linejoin="round"/>
      </svg>
      <p class="mission-item" style="left:108px;top:116px"><strong>We provide</strong> training and resources to anyone interested Arts, Education and Entrepreneurship.</p>

      <svg class="mission-icon" style="left:466px;top:34px" viewBox="0 0 34 34" aria-hidden="true">
        <text x="17" y="30" text-anchor="middle" font-family="Open Sans, sans-serif" font-weight="700" font-size="34" fill="var(--green)">?</text>
      </svg>
      <p class="mission-item" style="left:530px;top:16px"><strong>We help</strong> entrepreneur's start and grow their businesses in a tax efficient and appropriate way.</p>

      <svg class="mission-icon" style="left:466px;top:112px" viewBox="0 0 34 34" aria-hidden="true">
        <rect x="3" y="3" width="28" height="28" rx="3" fill="none" stroke="var(--green)" stroke-width="2.4"/>
        <circle cx="17" cy="13" r="5" fill="var(--green)"/>
        <path d="M8 29c1-6 5-9 9-9s8 3 9 9z" fill="var(--green)"/>
      </svg>
      <p class="mission-item" style="left:530px;top:98px"><strong>We work</strong> with all levels of local government to promote our community and create a fertile environment for growth.</p>
    </section>

    <div class="band band-appeal"></div>
    <p class="appeal-text">Every day, we look for ways to help our local businesses grow and expand, but we need you by our side. As an KRTLO Member, you can help provide training, education and support, and you can give our many businesses a chance to grow and our citizens the opportunity to experience big town amenities and events in a small town. Members' regular monthly gifts provide a consistent, reliable income stream that allows us to spend less time fundraising—and more time helping our businesses and community. Becoming an KRTLO Member is an easy, efficient and tax-deductible way to make a difference for our community all year long. Please donate today.</p>
  </main>
</body>
</html>
```